Webdesign für Getränkesofortlieferant
Zielgruppe
kistenbote ist ein Getränkesofortlieferant. Wir suchen ein hochwertiges Design für unsere Jobwebseite. Unsere Zielgruppe sind daher alle Bewerber, die sich für Jobs im Lager/in der Auslieferung interessieren sowie Bewerber, die sich für Jobs im Headquarter interessieren (z.B. im Marketing, in der IT, Finance etc.).
Aufgabenstellung
siehe Anhang

```html
<!DOCTYPE html>
<html lang="de">
<head>
<meta charset="utf-8">
<title>kistenbote – Jobwebseite</title>
<link href="https://fonts.googleapis.com/css2?family=Titillium+Web:ital,wght@0,300;0,400;0,600;1,300&family=Open+Sans:ital,wght@0,400;0,600;1,400&display=swap" rel="stylesheet">
<style>
:root{
  --green:#8d9b22;
  --green-light:#b3bf55;
  --magenta:#8c1f7d;
  --orange:#e5612c;
  --dark:#3d3d3b;
  --darker:#2f2f2e;
  --grey:#a8a8a6;
  --grey-mid:#c8c8c6;
  --light:#f1f1f0;
  --paper:#ffffff;
  --text:#555;
  --stage:#ffffff;
}
*{box-sizing:border-box;margin:0;padding:0}
html,body{width:1200px;height:2400px;overflow:hidden;background:var(--stage)}
body{position:relative;font-family:"Open Sans",sans-serif;color:var(--text)}
.page{position:absolute;background:var(--paper);overflow:hidden;box-shadow:0 0 0 1px #e2e2e2,0 3px 10px rgba(0,0,0,.12)}
.h{font-family:"Titillium Web",sans-serif;font-weight:300;text-transform:uppercase;text-align:center;letter-spacing:.02em}
.h-green{color:var(--green)}
.rule{display:block;width:3em;height:1px;background:var(--magenta);margin:0 auto .8em}
.sub{font-style:italic;text-align:center;color:#888}
.photo{display:block}

/* photo areas: soft tonal fills */
.ph-street{background:
  radial-gradient(ellipse 24% 30% at 82% 66%,rgba(196,55,150,.9),transparent 72%),
  radial-gradient(ellipse 20% 16% at 84% 50%,rgba(245,245,245,.9),transparent 72%),
  radial-gradient(ellipse 18% 26% at 28% 72%,rgba(80,140,205,.85),transparent 70%),
  radial-gradient(ellipse 10% 34% at 42% 52%,rgba(45,55,75,.85),transparent 72%),
  radial-gradient(ellipse 30% 30% at 70% 18%,rgba(120,110,100,.7),transparent 70%),
  linear-gradient(180deg,#c8b79c 0%,#9d8a70 35%,#75695c 62%,#8d8882 100%)}
.ph-team{background:
  radial-gradient(ellipse 60% 20% at 50% 45%,rgba(60,70,95,.55),transparent 75%),
  radial-gradient(ellipse 70% 22% at 50% 75%,rgba(50,70,120,.7),transparent 75%),
  radial-gradient(ellipse 40% 12% at 40% 35%,rgba(220,190,170,.5),transparent 75%),
  linear-gradient(180deg,#6f7b55 0%,#a9a69a 25%,#8e8a86 50%,#4f5f82 78%,#c9c6c0 100%)}
.ph-van{background:
  radial-gradient(ellipse 26% 40% at 22% 50%,rgba(60,50,45,.75),transparent 72%),
  radial-gradient(ellipse 30% 30% at 72% 70%,rgba(176,42,140,.9),transparent 72%),
  radial-gradient(ellipse 18% 22% at 90% 80%,rgba(140,155,40,.85),transparent 72%),
  linear-gradient(170deg,#7b7f86 0%,#eeeeee 22%,#dedede 60%,#c9c9c9 100%)}
.ph-warehouse{background:
  radial-gradient(ellipse 22% 40% at 20% 60%,rgba(40,70,160,.85),transparent 72%),
  radial-gradient(ellipse 20% 35% at 50% 65%,rgba(235,200,40,.85),transparent 72%),
  radial-gradient(ellipse 20% 35% at 78% 60%,rgba(190,45,45,.85),transparent 72%),
  radial-gradient(ellipse 40% 20% at 50% 10%,rgba(230,230,235,.8),transparent 72%),
  linear-gradient(180deg,#8d97a8 0%,#4f5d82 40%,#5a4a3c 100%)}
.ph-office{background:
  radial-gradient(ellipse 30% 25% at 55% 70%,rgba(150,110,70,.75),transparent 72%),
  radial-gradient(ellipse 18% 30% at 25% 55%,rgba(60,60,70,.6),transparent 72%),
  radial-gradient(ellipse 18% 30% at 80% 50%,rgba(70,70,85,.55),transparent 72%),
  linear-gradient(180deg,#f2efea 0%,#ddd6cc 45%,#b9aa97 100%)}
.ph-cars{background:
  radial-gradient(ellipse 40% 18% at 50% 72%,rgba(205,90,170,.6),transparent 72%),
  radial-gradient(ellipse 50% 14% at 50% 62%,rgba(250,250,250,.9),transparent 72%),
  linear-gradient(180deg,#dfe3e8 0%,#a8b0ba 40%,#d6d9dd 58%,#9ea3a8 100%)}
.ph-crew{background:
  radial-gradient(ellipse 10% 10% at 18% 28%,rgba(175,205,80,.9),transparent 72%),
  radial-gradient(ellipse 10% 10% at 62% 30%,rgba(220,120,190,.9),transparent 72%),
  radial-gradient(ellipse 60% 18% at 50% 42%,rgba(215,180,160,.55),transparent 75%),
  radial-gradient(ellipse 70% 18% at 50% 58%,rgba(35,35,40,.7),transparent 75%),
  radial-gradient(ellipse 75% 24% at 50% 82%,rgba(60,85,135,.85),transparent 75%),
  linear-gradient(180deg,#f4f4f4 0%,#e6e6e6 40%,#8a93a6 70%,#d9d9d9 100%)}
.ph-portrait{background:
  radial-gradient(ellipse 22% 22% at 50% 32%,rgba(205,170,150,.9),transparent 72%),
  radial-gradient(ellipse 40% 30% at 50% 82%,rgba(55,55,60,.9),transparent 72%),
  linear-gradient(180deg,#e9e9e9,#d6d6d6)}
.ph-poster{background:
  radial-gradient(ellipse 40% 25% at 45% 40%,rgba(176,30,130,.85),transparent 72%),
  radial-gradient(ellipse 18% 18% at 80% 20%,rgba(140,155,40,.85),transparent 72%),
  linear-gradient(180deg,#fafafa,#f0eef0)}
.ph-map{background:#fff}
.frame{box-shadow:0 1px 3px rgba(0,0,0,.18)}

/* nav */
.nav{display:flex;align-items:center;height:2.6em;background:var(--dark);color:#ddd;font-family:"Titillium Web",sans-serif}
.nav .brand{display:flex;align-items:center;gap:.4em;padding:0 1em;font-size:1em;font-weight:600;color:var(--green-light);width:32%}
.nav .brand i{display:block;width:1.9em;height:1.9em;border-radius:50%;background:var(--green);border:.15em solid #fff}
.nav ul{list-style:none;display:flex;gap:3.2em;flex:1;font-size:.62em;letter-spacing:.03em}
.nav .shop{background:var(--green);height:100%;display:flex;align-items:center;padding:0 2.2em;font-size:.62em;color:#fff}
.foot{display:flex;gap:2em;background:var(--darker);color:#bbb;font-size:.45em;padding:.6em 3em}

/* main page */
.main{left:420px;top:73px;width:370px;font-size:10px}
.hero{position:relative;height:250px}
.hero .photo{position:absolute;inset:0}
.hero .tag{position:absolute;left:125px;top:82px;background:var(--magenta);color:#fff;font-family:"Titillium Web",sans-serif;font-size:12px;padding:2px 7px;letter-spacing:.03em}
.hero .box{position:absolute;left:125px;top:102px;width:172px;background:rgba(40,40,40,.84);color:#eee;padding:6px 8px 9px;font-size:5px;line-height:1.5}
.hero .box b{display:block;font-family:"Titillium Web",sans-serif;font-weight:400;font-size:9px;margin-bottom:2px}
.hero .btn{display:inline-block;margin-top:6px;background:var(--green);color:#fff;font-style:italic;font-size:5px;padding:2px 8px}
.arrow{position:absolute;width:11px;height:11px;border-radius:50%;background:rgba(255,255,255,.85)}
.arrow svg{display:block;width:11px;height:11px}
.sec{padding:22px 18px 18px;text-align:center}
.sec .h{font-size:11px;margin-bottom:2px}
.history{height:300px;background:#f7f7f6;padding-top:90px}
.history .map{width:70px;height:92px;margin:20px auto 6px;border-radius:30% 40% 35% 45%/30% 35% 45% 40%;box-shadow:0 0 0 1px #eee}
.years{display:flex;justify-content:center;align-items:center;gap:10px;font-size:5px;color:var(--magenta)}
.years i{display:block;width:6px;height:6px;border-radius:50%;border:1px solid var(--green-light)}
.small-note{font-size:5.5px;color:#999;margin:8px 0 4px}
.places{height:205px}
.places .strip{display:flex;align-items:center;justify-content:center;margin:14px 0 10px}
.places .strip span{height:55px;width:80px;opacity:.75}
.places .strip span.c{height:80px;width:115px;opacity:1}
.places .nav2{display:flex;justify-content:center;align-items:center;gap:40px}
.places .nav2 i{display:block;width:6px;height:6px;border-radius:50%;border:1px solid var(--green-light)}
.places .city{font-family:"Titillium Web",sans-serif;color:var(--green);font-size:10px}
.usp{background:var(--grey);height:190px;color:#fff}
.usp .h{color:var(--magenta)}
.usp .cols{display:flex;margin-top:18px}
.usp .col{flex:1;padding:0 6px}
.usp .ico{width:18px;height:18px;margin:0 auto 10px}
.usp .t{font-family:"Titillium Web",sans-serif;font-size:7px;margin-bottom:7px}
.usp p{font-size:4.2px;line-height:1.5}
.pstrip{display:flex;height:66px}
.pstrip span{flex:1}
.follow{background:var(--dark);height:194px;color:#fff}
.follow .h{color:#fff}
.follow .hd{color:var(--green-light);font-size:5.5px;margin-top:2px}
.embed{width:108px;margin:16px auto 0;background:#fff;text-align:left;padding-bottom:4px}
.embed .cover{height:28px}
.embed .line{height:3px;background:#e4e4e4;margin:4px 5px 0}
.embed .thumbs{display:flex;gap:2px;margin:4px 5px 0}
.embed .thumbs span{width:8px;height:8px;background:#d5d5d5}

/* left screens */
.mini{font-size:6px}
.mini .nav{height:2.3em}
.mini-a{left:96px;top:218px;width:232px;height:165px}
.mini-b{left:42px;top:405px;width:234px;height:165px}
.mini .photo{position:absolute;left:0;right:0;top:14px;bottom:6px}
.mini .card{position:absolute;background:rgba(40,40,40,.85);color:#ddd;font-size:3.6px;line-height:1.5;padding:5px}
.mini .card b{display:block;font-family:"Titillium Web",sans-serif;font-weight:400;font-size:5px;color:var(--orange);margin-bottom:2px}
.mini .foot{position:absolute;bottom:0;left:0;right:0}

/* right screens */
.tl{left:800px;width:378px;height:272px;background:var(--light);font-size:10px}
.tl-a{top:450px}.tl-b{top:752px}
.tl .h{font-size:11px;margin-top:4px}
.tl .circ{position:absolute;width:72px;height:72px;border-radius:50%}
.tl .de{position:absolute;width:55px;height:72px;background:#fff;border-radius:30% 40% 35% 45%/30% 35% 45% 40%}
.tl .line{position:absolute;left:42px;right:52px;height:1px;background:var(--green)}
.tl .lbl{position:absolute;font-size:6px;color:#999}
.tl .yr{position:absolute;font-size:5px;color:var(--magenta);display:flex;gap:8px;align-items:center}
.tl .yr i{display:block;width:6px;height:6px;border-radius:50%;border:1px solid var(--green-light)}

/* bottom pages */
.sub-page{top:1458px;width:255px;font-size:6px}
.p1{left:68px;height:605px}
.p2{left:351px;height:869px}
.p3{left:634px;height:670px}
.p4{left:915px;height:412px;background:var(--light)}
.sub-page .sec{padding:16px 14px 14px}
.sub-page .h{font-size:7.5px}
.tiny{font-size:3.6px;line-height:1.5;color:#777;text-align:center}
.cards{display:flex;gap:18px;justify-content:center;margin-top:14px}
.jobcard{position:relative;width:98px}
.jobcard .photo{height:62px}
.jobcard .lab{background:var(--green);color:#fff;font-family:"Titillium Web",sans-serif;font-size:5px;text-align:center;padding:4px 0}
.badge{position:absolute;width:17px;height:17px;border-radius:50%;background:var(--orange);color:#fff;font-size:2.6px;display:flex;align-items:center;justify-content:center;text-align:center;line-height:1.2}
.grey-band{background:var(--grey);color:#fff}
.grey-band .h{color:#f4f4f4}
.perks{display:grid;grid-template-columns:repeat(3,1fr);row-gap:18px;margin-top:16px;text-align:center}
.perks .ico{width:18px;height:18px;margin:0 auto 5px}
.perks .t{font-family:"Titillium Web",sans-serif;font-size:5px}
.perks .d{font-size:2.8px;opacity:.8;margin-top:1px}
.contact{position:relative;height:170px;margin-top:14px}
.contact .photo{position:absolute;inset:0}
.contact .box{position:absolute;right:12px;bottom:10px;width:110px;background:rgba(140,31,125,.92);color:#fff;padding:6px 7px;font-size:3.6px;line-height:1.5}
.contact .box b{display:block;font-family:"Titillium Web",sans-serif;font-weight:400;font-size:6px;margin-bottom:2px}
.contact .row{display:flex;align-items:center;gap:3px;font-weight:600;font-size:4px;margin-top:3px}
.contact .row svg{width:5px;height:5px}
.contact .badge{right:12px;bottom:72px}
.panel{background:#fff;box-shadow:0 0 0 1px #eee;display:flex;margin-top:12px;font-size:3.4px;text-align:left}
.panel .filters{width:30%;padding:5px;border-right:1px solid #eee;line-height:1.7;color:#777}
.panel .filters b,.panel .list b{color:var(--green);display:block;font-weight:600}
.panel .mid{width:27%;padding:5px;background:var(--light);display:flex;flex-direction:column;align-items:center;justify-content:space-between}
.panel .mid .m{width:42px;height:50px;background:#fff;border-radius:30% 40% 35% 45%/30% 35% 45% 40%}
.panel .count{background:var(--green-light);color:#fff;text-align:center;width:100%;padding:3px;font-size:3px}
.panel .count span{display:block;font-size:10px;font-family:"Titillium Web",sans-serif;color:var(--dark)}
.panel .list{flex:1;padding:5px;line-height:1.6;color:#777}
.panel .list .city{color:var(--magenta);font-weight:600;margin-top:3px}
.panel .list .r{display:flex;justify-content:space-between;align-items:center}
.panel .list .go{width:14px;height:3px;background:var(--green)}
.steps{display:flex;margin-top:16px;position:relative}
.steps::before{content:"";position:absolute;left:12%;right:12%;top:7px;height:1px;background:var(--green)}
.step{flex:1;text-align:center;position:relative}
.step .ico{width:12px;height:12px;margin:0 auto 4px;background:#fff}
.step .n{font-family:"Titillium Web",sans-serif;color:var(--magenta);font-size:8px}
.step .t{color:var(--magenta);font-size:3.6px;font-weight:600;line-height:1.3}
.step .d{font-size:2.8px;color:#888;margin-top:3px;line-height:1.4}
.jobs3{display:flex;gap:3px;margin-top:12px}
.jobs3 .c{flex:1;background:#fff;color:#777;text-align:left}
.jobs3 .photo{height:46px}
.jobs3 .c div{padding:4px;font-size:3px;line-height:1.7}
.jobs3 .c b{color:var(--green);font-weight:600;font-size:3.4px}
.more{color:var(--magenta);font-size:3.4px;margin-top:10px}
.more i{display:block;width:9px;height:9px;border-radius:50%;background:var(--magenta);margin:3px auto 0}
.people{display:flex;background:var(--light);height:140px;align-items:center}
.people .photo{width:110px;height:140px}
.people .q{flex:1;padding-right:12px;font-size:3.6px;line-height:1.5;color:#777}
.people .q .h{text-align:left;color:var(--magenta);font-size:7px;line-height:1.1;margin-bottom:5px}
.dots{display:flex;gap:4px;margin-top:8px}
.dots i{width:3px;height:3px;border-radius:50%;background:#ccc}
.dots i.on{background:var(--green)}
.table{flex:1;padding:5px;font-size:3.2px;color:#777;line-height:1.75}
.table .r{display:grid;grid-template-columns:1.7fr 1fr .8fr .9fr;align-items:center}
.table .r.hd{color:var(--magenta);font-weight:600}
.table .go{height:3px;background:var(--green)}
.crew-strip{display:flex;gap:2px;margin-top:4px;height:40px}
.crew-strip span{flex:1}
.depts{display:flex;align-items:center;justify-content:center;gap:6px;margin-top:16px}
.depts .ar{width:7px;height:7px;border-radius:50%;border:1px solid var(--grey-mid)}
.dept{width:95px}
.dept .photo{height:65px}
.dept .lab{background:var(--green);color:#fff;text-align:center;padding:6px 4px;height:48px}
.dept .lab b{display:block;font-family:"Titillium Web",sans-serif;font-weight:400;font-size:5px;margin-bottom:3px}
.dept .lab span{font-size:3.4px}
.faq{margin:12px 40px 0;text-align:left}
.faq .row{display:flex;gap:5px;border-bottom:1px solid var(--magenta);padding:3px 0;font-size:4px;color:var(--dark)}
.faq .row span{color:var(--magenta)}
.faq p{font-size:2.8px;line-height:1.5;color:#777;margin:4px 0 4px 10px}
.faq p b{color:var(--dark)}
</style>
</head>
<body>

<!-- Left: team teaser screen -->
<div class="page mini mini-a">
  <div class="nav"><span class="brand"><i></i>kistenbote</span><ul><li>UNTERNEHMEN</li><li>JOBS</li><li>FAQ</li></ul><span class="shop">UNSER SHOP</span></div>
  <div class="photo ph-team" role="img" aria-label="Gruppenfoto des gesamten Teams im Freien"></div>
  <div class="card" style="left:118px;top:50px;width:84px">
    <b>KOMM INS TEAM</b>
    Wir suchen Menschen, die mit uns den Getränkehandel neu denken. Ob im Lager, auf der Straße oder im Büro – bei uns zählt jeder Einzelne.<br><br>Werde Teil unseres Teams und wachse mit uns.
  </div>
  <div class="foot"><span>© kistenbote GmbH</span><span>IMPRESSUM</span><span>DATENSCHUTZ</span></div>
</div>

<!-- Left: city teaser screen -->
<div class="page mini mini-b">
  <div class="nav"><span class="brand"><i></i>kistenbote</span><ul><li>UNTERNEHMEN</li><li>JOBS</li><li>FAQ</li></ul><span class="shop">UNSER SHOP</span></div>
  <div class="photo ph-van" role="img" aria-label="Lächelnder Fahrer im Lieferwagen mit Firmenbeschriftung"></div>
  <div class="card" style="left:115px;top:60px;width:82px">
    <b style="color:#fff">DEINE STADT WIRD DICH LIEBEN!</b>
    Mit jeder Lieferung bringst Du Freude in die Stadt. Komm zu uns und liefere Getränke schnell zu unseren Kunden.<br><span style="color:var(--green-light)">Bewirb dich jetzt und werde unser Held!</span>
  </div>
</div>

<!-- Main company page -->
<div class="page main">
  <div class="nav"><span class="brand"><i></i>kistenbote</span><ul><li>UNTERNEHMEN</li><li>JOBS</li><li>FAQ</li></ul><span class="shop">UNSER SHOP</span></div>
  <div class="hero">
    <div class="photo ph-street" role="img" aria-label="Lieferant mit Sackkarre und Getränkekisten in einer Altstadtgasse, daneben ein Lieferwagen"></div>
    <div class="tag">GETRÄNKE FÜR ALLE.</div>
    <div class="box"><b>SOFORT.</b>Der Wasservorrat für das Büro, das Bier für den Grillabend oder die Cola für zwischendurch – wir liefern innerhalb von 120 Minuten. Und das alles egal in welches Stockwerk, ohne Liefergebühr und zu Preisen wie im Supermarkt.<br><span class="btn">Lasst uns den Getränkehandel revolutionieren!</span></div>
    <span class="arrow" style="left:10px;top:120px"><svg viewBox="0 0 11 11"><path d="M6.5 3 4 5.5 6.5 8" fill="none" stroke="#8d9b22" stroke-width="1"/></svg></span>
    <span class="arrow" style="right:10px;top:120px"><svg viewBox="0 0 11 11"><path d="M4.5 3 7 5.5 4.5 8" fill="none" stroke="#8d9b22" stroke-width="1"/></svg></span>
  </div>

  <section class="sec history">
    <span class="rule"></span>
    <h2 class="h h-green">Die Geschichte der kistenbote</h2>
    <p class="sub" style="font-size:6px">Bald auch in Deiner Stadt?</p>
    <div class="map ph-map" role="img" aria-label="Umriss von Deutschland mit Punkt für Münster"></div>
    <p class="small-note">Gründung in Münster</p>
    <div class="years"><i></i>2016<i></i></div>
  </section>

  <section class="sec places">
    <span class="rule"></span>
    <h2 class="h h-green">Die Standorte</h2>
    <div class="strip">
      <span class="ph-office" role="img" aria-label="Lagerhalle mit Mitarbeitern"></span>
      <span class="c ph-warehouse frame" role="img" aria-label="Getränkelager mit gestapelten Kisten in Münster"></span>
      <span class="ph-cars" role="img" aria-label="Lieferwagen vor dem Standortgebäude"></span>
    </div>
    <div class="nav2"><i></i><div><div class="city">Münster</div><div style="font-size:5px;color:#999">zu den Jobs in Münster</div></div><i></i></div>
  </section>

  <section class="sec usp">
    <span class="rule"></span>
    <h2 class="h">Was uns ausmacht</h2>
    <div class="cols">
      <div class="col">
        <svg class="ico" viewBox="0 0 18 18" fill="none" stroke="#fff" stroke-width="1"><circle cx="9" cy="10" r="6"/><path d="M9 10V6.5M7.5 2.5h3M9 2.5v1.5"/></svg>
        <div class="t">LIEFERUNG IN<br>120 MINUTEN</div>
        <p>Wir liefern innerhalb 120 Minuten ab der Bestellung. Immer und ohne Aufpreis! (Montag bis Samstag von 9 bis 21 Uhr)</p>
      </div>
      <div class="col">
        <svg class="ico" viewBox="0 0 18 18" fill="none" stroke="#fff" stroke-width="1"><path d="M2 6h9v6H2zM11 8h3l2 2v2h-5"/><circle cx="5" cy="13" r="1.3"/><circle cx="13" cy="13" r="1.3"/></svg>
        <div class="t">KEINE<br>LIEFERGEBÜHR</div>
        <p>Bei uns gibt es keine Liefergebühr. Alle Bestellungen werden kostenfrei bis an die Wohnungs- oder Haustüre geliefert. Egal, in welchem Stockwerk sich diese befindet.</p>
      </div>
      <div class="col">
        <svg class="ico" viewBox="0 0 18 18" fill="none" stroke="#fff" stroke-width="1"><path d="M3 8h12v7H3zM5 8V4h2v4M11 8V4h2v4"/></svg>
        <div class="t">BEQUEME<br>PFANDRÜCKGABE</div>
        <p>Leergut der Kunden nehmen wir einfach wieder mit. Der Pfandbetrag wird dann direkt von der Rechnung abgezogen.</p>
      </div>
    </div>
  </section>

  <div class="pstrip">
    <span class="ph-office" role="img" aria-label="Büro mit großen Fenstern"></span>
    <span class="ph-van" role="img" aria-label="Lieferwagen in der Stadt"></span>
    <span class="ph-poster" role="img" aria-label="Werbeplakat Boten werben Boten"></span>
    <span class="ph-cars" role="img" aria-label="Mitarbeiter im Flur des Lagers"></span>
    <span class="ph-van" role="img" aria-label="Lieferwagen von hinten beim Beladen"></span>
  </div>

  <section class="sec follow">
    <span class="rule"></span>
    <h2 class="h" style="font-weight:400">Folgt uns!</h2>
    <p style="font-style:italic;font-size:6px">kistenbote in unseren Kanälen</p>
    <p class="hd">@wirsindkistenbote</p>
    <div class="embed">
      <div class="cover ph-team" role="img" aria-label="Titelbild des Profils mit Teamfoto"></div>
      <div class="line" style="width:60%"></div>
      <div class="line" style="width:40%"></div>
      <div class="thumbs"><span></span><span></span><span></span><span></span><span></span><span></span><span></span></div>
    </div>
  </section>
  <div class="foot"><span>© kistenbote GmbH</span><span>IMPRESSUM</span><span>DATENSCHUTZ</span></div>
</div>

<!-- Right: timeline, first state -->
<div class="page tl tl-a">
  <div style="padding-top:40px"><span class="rule"></span><h2 class="h h-green">Die Geschichte der kistenbote</h2><p class="sub" style="font-size:6.5px">Bald auch in Deiner Stadt?</p></div>
  <span class="circ ph-warehouse" style="left:65px;top:108px" role="img" aria-label="Lagerhalle mit Getränkekisten, Standort Münster"></span>
  <svg style="position:absolute;left:136px;top:120px" width="52" height="24"><path d="M0 1h20l20 20" fill="none" stroke="#8d9b22" stroke-width=".8"/></svg>
  <span class="de" style="left:175px;top:110px" role="img" aria-label="Umriss von Deutschland"></span>
  <span class="lbl" style="left:155px;top:228px">Gründung in Münster</span>
  <span class="line" style="top:240px"></span>
  <span class="yr" style="left:165px;top:252px"><i></i>2016<i></i></span>
</div>

<!-- Right: timeline, second state -->
<div class="page tl tl-b">
  <div style="padding-top:40px"><span class="rule"></span><h2 class="h h-green">Die Geschichte der kistenbote</h2><p class="sub" style="font-size:6.5px">Bald auch in Deiner Stadt?</p></div>
  <span class="circ ph-warehouse" style="left:65px;top:108px;opacity:.45" role="img" aria-label="Lagerhalle in Münster, abgeblendet"></span>
  <svg style="position:absolute;left:136px;top:120px" width="52" height="24"><path d="M0 1h20l20 20" fill="none" stroke="#8d9b22" stroke-width=".8"/></svg>
  <span class="de" style="left:175px;top:110px" role="img" aria-label="Umriss von Deutschland"></span>
  <svg style="position:absolute;left:190px;top:150px" width="60" height="12"><path d="M0 6h58" fill="none" stroke="#8d9b22" stroke-width=".8"/></svg>
  <span class="circ ph-cars" style="left:222px;top:132px" role="img" aria-label="Lieferwagenflotte vor dem Standort Düsseldorf"></span>
  <span class="lbl" style="left:45px;top:228px">Gründung in Münster</span>
  <span class="lbl" style="left:152px;top:226px">Expansion in Düsseldorf</span>
  <span class="line" style="top:240px"></span>
  <span class="yr" style="left:62px;top:252px">2016</span>
  <span class="yr" style="left:165px;top:252px"><i></i>2017<i></i></span>
</div>

<!-- Jobs overview page -->
<div class="page sub-page p1">
  <div class="nav"><span class="brand"><i></i>kistenbote</span><ul><li>UNTERNEHMEN</li><li>JOBS</li><li>FAQ</li></ul><span class="shop">UNSER SHOP</span></div>
  <section class="sec">
    <span class="rule"></span>
    <h2 class="h" style="color:var(--dark)">Werde Teil unseres Teams</h2>
    <p class="tiny" style="margin-top:6px">BITTE KLICKE AUF DEN BEREICH, DER DICH INTERESSIERT –<br>DIE VERFÜGBAREN JOBS WERDEN DIR DANN ANGEZEIGT.</p>
    <div class="cards">
      <div class="jobcard"><div class="photo ph-office" role="img" aria-label="Kollegen im Büro am Besprechungstisch"></div><div class="lab">CORPORATE</div><span class="badge" style="left:-3px;top:52px">JETZT BEWERBEN</span></div>
      <div class="jobcard"><div class="photo ph-warehouse" role="img" aria-label="Mitarbeiter mit Warnweste im Lager"></div><div class="lab">AUSLIEFERUNG /LAGER</div><span class="badge" style="left:-3px;top:52px">JETZT BEWERBEN</span></div>
    </div>
  </section>
  <section class="sec grey-band" style="padding-top:22px;padding-bottom:22px">
    <span class="rule"></span>
    <h2 class="h" style="font-size:6.5px">kistenbote als Arbeitgeber</h2>
    <div class="perks">
      <div><svg class="ico" viewBox="0 0 18 18" fill="none" stroke="#fff" stroke-width=".8"><circle cx="9" cy="9" r="7"/><path d="M9 9V4.5M9 9l3 2"/></svg><div class="t">Flexible Arbeitszeiten</div><div class="d">Voll- oder Teilzeit möglich</div></div>
      <div><svg class="ico" viewBox="0 0 18 18" fill="none" stroke="#fff" stroke-width=".8"><circle cx="6" cy="8" r="3.5"/><circle cx="12" cy="8" r="3.5"/></svg><div class="t">Motiviertes Team</div><div class="d">Gemeinsam etwas bewegen</div></div>
      <div><svg class="ico" viewBox="0 0 18 18" fill="none" stroke="#fff" stroke-width=".8"><path d="M3 9h12v5H3zM4 9l2-4h6l2 4"/></svg><div class="t">moderne Technik</div><div class="d">neueste Fahrzeuge</div></div>
      <div><svg class="ico" viewBox="0 0 18 18" fill="none" stroke="#fff" stroke-width=".8"><path d="M2 10l4-3 3 2 3-2 4 3-4 3-3-2-3 2z"/></svg><div class="t">Flache Hierarchien</div><div class="d">kurze Wege, schnelle Entscheidungen</div></div>
      <div><svg class="ico" viewBox="0 0 18 18" fill="none" stroke="#fff" stroke-width=".8"><path d="M9 2v14M4 16l5-6 5 6"/></svg><div class="t">Gutes Betriebsklima</div><div class="d">Team-Events und Feiern</div></div>
      <div><svg class="ico" viewBox="0 0 18 18" fill="none" stroke="#fff" stroke-width=".8"><path d="M2 2v14h14M4 13l4-4 3 2 5-6"/></svg><div class="t">Starkes Wachstum</div><div class="d">neue Städte jedes Jahr</div></div>
    </div>
  </section>
  <section class="sec">
    <span class="rule"></span>
    <h2 class="h" style="color:var(--dark)">Kontakt</h2>
    <div class="contact">
      <div class="photo ph-crew" role="img" aria-label="Team des Personalbereichs mit Sprechblasen-Schildern"></div>
      <span class="badge">WIR FREUEN UNS AUF DICH</span>
      <div class="box"><b>Fragen?</b>Viele Antworten findet ihr auch in den FAQs – Du kannst Dich aber auch gerne direkt an uns wenden.
        <div class="row"><svg viewBox="0 0 6 6"><path d="M1 .5h1.3l.5 1.4-.8.6a3 3 0 0 0 1.5 1.5l.6-.8 1.4.5V5A.5.5 0 0 1 5 5.5 4.5 4.5 0 0 1 .5 1 .5.5 0 0 1 1 .5z" fill="#fff"/></svg>0251 555 01 234</div>
        <div class="row"><svg viewBox="0 0 6 6"><rect x=".5" y="1" width="5" height="4" fill="none" stroke="#fff" stroke-width=".6"/><path d="M.5 1l2.5 2 2.5-2" fill="none" stroke="#fff" stroke-width=".6"/></svg>personal@kistenbote.de</div>
      </div>
    </div>
  </section>
  <div class="foot"><span>© kistenbote GmbH</span><span>IMPRESSUM</span><span>DATENSCHUTZ</span></div>
</div>

<!-- Jobs delivery / warehouse page -->
<div class="page sub-page p2">
  <div class="nav"><span class="brand"><i></i>kistenbote</span><ul><li>UNTERNEHMEN</li><li>JOBS</li><li>FAQ</li></ul><span class="shop">UNSER SHOP</span></div>
  <section class="sec" style="background:var(--light)">
    <h2 class="h" style="color:var(--dark)">Jobs im Bereich Auslieferung / Lager</h2>
    <div class="panel">
      <div class="filters"><b>STANDORT</b>alle anzeigen<br>Bochum<br>Dortmund<br>Düsseldorf<br>Essen<br>Köln<br>Münster<br>Wuppertal<br><b style="margin-top:4px">BEREICH</b>Auslieferung<br>Lager</div>
      <div class="mid"><span style="color:var(--green)">KARTENANSICHT</span><span class="m ph-map" role="img" aria-label="Deutschlandkarte mit Standortpunkten"></span><div class="count">VERFÜGBARE JOBS BEI KISTENBOTE<span>36</span></div></div>
      <div class="list"><b>DERZEIT SUCHEN WIR …</b>
        <div class="city">Bochum</div><div class="r">Auslieferungsfahrer<span class="go"></span></div><div class="r">Lagerist<span class="go"></span></div><div class="r">Schichtleiter<span class="go"></span></div>
        <div class="city">Dortmund</div><div class="r">Auslieferungsfahrer<span class="go"></span></div><div class="r">Lagerist<span class="go"></span></div><div class="r">Schichtleiter<span class="go"></span></div>
        <div class="city">Düsseldorf</div><div class="r">Auslieferungsfahrer<span class="go"></span></div><div class="r">Lagerist<span class="go"></span></div><div class="r">Schichtleiter<span class="go"></span></div>
      </div>
    </div>
  </section>
  <section class="sec" style="padding-top:22px">
    <span class="rule"></span>
    <h2 class="h h-green">Unser Bewerbungsprozess</h2>
    <p class="sub" style="font-size:4px">Vier Schritte zum Heldenstatus!</p>
    <div class="steps">
      <div class="step"><svg class="ico" viewBox="0 0 12 12" fill="none" stroke="#8d9b22" stroke-width=".8"><rect x="2" y="2.5" width="8" height="5.5"/><path d="M6 8v2M4 10h4"/></svg><div class="n">1.</div><div class="t">ONLINE<br>BEWERBUNG</div><div class="d">Fülle einfach unser Formular aus und sende es ab.</div></div>
      <div class="step"><svg class="ico" viewBox="0 0 12 12" fill="none" stroke="#8d9b22" stroke-width=".8"><path d="M3 2v8M9 2v8M3 5h6"/></svg><div class="n">2.</div><div class="t">EINLADUNG ZUM<br>PROBEARBEITEN</div><div class="d">Du lernst das Team und die Abläufe kennen.</div></div>
      <div class="step"><svg class="ico" viewBox="0 0 12 12" fill="none" stroke="#8d9b22" stroke-width=".8"><path d="M3 1.5h5l2 2v7H3zM4.5 6h4M4.5 8h4"/></svg><div class="n">3.</div><div class="t">VERTRAGS-<br>ABSCHLUSS</div><div class="d">Wir besprechen alle Details und unterschreiben.</div></div>
      <div class="step"><svg class="ico" viewBox="0 0 12 12" fill="none" stroke="#8d9b22" stroke-width=".8"><path d="M6 1.5 10 3v3.5c0 2-2 3.5-4 4-2-.5-4-2-4-4V3z"/></svg><div class="n">4.</div><div class="t">HELD<br>SEIN</div><div class="d">Bringe als Getränkeheld Freude in Deine Stadt.</div></div>
    </div>
  </section>
  <section class="sec grey-band" style="padding-top:20px">
    <span class="rule"></span>
    <h2 class="h">Unsere Berufe</h2>
    <div class="jobs3">
      <div class="c"><span class="photo ph-van" role="img" aria-label="Lieferwagen vor Gebäude"></span><div><b>AUSLIEFERUNGSFAHRER</b><br>✓ Getränke ausliefern<br>✓ Voll-/Teilzeit<br>✓ 450€-Basis</div></div>
      <div class="c"><span class="photo ph-warehouse" role="img" aria-label="Lagerist zwischen Kistenstapeln"></span><div><b>LAGERIST</b><br>✓ Bestellungen packen<br>✓ Voll-/Teilzeit<br>✓ 450€-Basis</div></div>
      <div class="c"><span class="photo ph-poster" role="img" aria-label="Mitarbeiterin im Verkaufsraum"></span><div><b>KOMMISSIONIERUNG</b><br>✓ Ware zusammenstellen<br>✓ Voll-/Teilzeit<br>✓ 450€-Basis</div></div>
    </div>
    <div class="more">alle Jobs anzeigen<i></i></div>
  </section>
  <div class="people">
    <div class="photo ph-portrait" role="img" aria-label="Porträt eines jungen Mitarbeiters im dunklen T-Shirt"></div>
    <div class="q"><h3 class="h">Menschen<br>bei kistenbote</h3>„Als Auslieferungsfahrer lerne ich meine Stadt jeden Tag besser kennen. Ich bin an der frischen Luft und unsere Kunden freuen sich immer, wenn ich mit ihrer Bestellung komme.“<br><br>Timo, 24 J. Düsseldorf<br>Auslieferungsfahrer<div class="dots"><i></i><i></i><i></i><i></i><i class="on"></i></div></div>
  </div>
  <section class="sec">
    <span class="rule"></span>
    <h2 class="h h-green">Ansprechpartner</h2>
    <div class="contact" style="height:180px">
      <div class="photo ph-crew" role="img" aria-label="Team des Personalbereichs mit Sprechblasen-Schildern"></div>
      <span class="badge" style="bottom:80px">WIR FREUEN UNS AUF DICH</span>
      <div class="box">Das Team Personal steht Dir bei allen Fragen zur Verfügung!
        <div class="row"><svg viewBox="0 0 6 6"><path d="M1 .5h1.3l.5 1.4-.8.6a3 3 0 0 0 1.5 1.5l.6-.8 1.4.5V5A.5.5 0 0 1 5 5.5 4.5 4.5 0 0 1 .5 1 .5.5 0 0 1 1 .5z" fill="#fff"/></svg>0251 555 01 234</div>
        <div class="row"><svg viewBox="0 0 6 6"><rect x=".5" y="1" width="5" height="4" fill="none" stroke="#fff" stroke-width=".6"/><path d="M.5 1l2.5 2 2.5-2" fill="none" stroke="#fff" stroke-width=".6"/></svg>personal@kistenbote.de</div>
      </div>
    </div>
  </section>
  <div class="foot"><span>© kistenbote GmbH</span><span>IMPRESSUM</span><span>DATENSCHUTZ</span></div>
</div>

<!-- Jobs corporate page -->
<div class="page sub-page p3">
  <div class="nav"><span class="brand"><i></i>kistenbote</span><ul><li>UNTERNEHMEN</li><li>JOBS</li><li>FAQ</li></ul><span class="shop">UNSER SHOP</span></div>
  <section class="sec" style="background:var(--light)">
    <h2 class="h" style="color:var(--dark)">Jobs im Bereich Corporate</h2>
    <p class="sub" style="font-size:4px">im Headquarter Münster</p>
    <div class="panel">
      <div class="filters"><b>BEREICH</b>alle anzeigen<br>Business Development<br>Einkauf<br>Finance<br>IT<br>Marketing<br>Operations<br><b style="margin-top:4px">ART</b>Festanstellung<br>Praktikum<br>Werkstudent</div>
      <div class="mid" style="justify-content:flex-end"><div class="count">VERFÜGBARE JOBS BEI KISTENBOTE<span>36</span></div></div>
      <div class="table"><b style="color:var(--green);font-weight:600">DERZEIT SUCHEN WIR …</b>
        <div class="r hd"><span>Job</span><span>Abteilung</span><span>Art</span><span></span></div>
        <div class="r"><span>Event Manager</span><span>Marketing</span><span>Vollzeit</span><span class="go"></span></div>
        <div class="r"><span>Head of Content</span><span>Marketing</span><span>Vollzeit</span><span class="go"></span></div>
        <div class="r"><span>Marketing Manager</span><span>Marketing</span><span>Vollzeit</span><span class="go"></span></div>
        <div class="r"><span>Senior Designer</span><span>Marketing</span><span>Vollzeit</span><span class="go"></span></div>
        <div class="r"><span>Community Manager</span><span>Marketing</span><span>Vollzeit</span><span class="go"></span></div>
        <div class="r"><span>Marketing Analyst</span><span>Marketing</span><span>Praktikum</span><span class="go"></span></div>
        <div class="r"><span>Social Media</span><span>Marketing</span><span>Praktikum</span><span class="go"></span></div>
      </div>
    </div>
    <div class="crew-strip">
      <span class="ph-office" role="img" aria-label="Meeting im Konferenzraum"></span>
      <span class="ph-crew" role="img" aria-label="Gruppe von Kollegen"></span>
      <span class="ph-team" role="img" aria-label="Großes Teamfoto"></span>
    </div>
  </section>
  <section class="sec" style="padding-top:26px">
    <span class="rule"></span>
    <h2 class="h" style="color:var(--dark)">Unsere Abteilungen</h2>
    <div class="depts">
      <span class="ar"></span>
      <div class="dept"><div class="photo ph-crew" role="img" aria-label="Marketingteam in Jeans vor weißer Wand"></div><div class="lab"><b>TEAM MARKETING</b><span>„Wir sorgen für einen reibungslosen Ablauf“</span></div></div>
      <div class="dept"><div class="photo ph-crew" role="img" aria-label="IT-Team in Jeans vor weißer Wand"></div><div class="lab"><b>TEAM IT</b><span>„Gemeinsam arbeiten wir an Lösungen für spannende Herausforderungen“</span></div></div>
      <span class="ar"></span>
    </div>
  </section>
  <section class="sec" style="padding-top:26px">
    <span class="rule"></span>
    <h2 class="h" style="color:var(--dark)">Kontakt</h2>
    <div class="contact">
      <div class="photo ph-crew" role="img" aria-label="Team des Personalbereichs mit Sprechblasen-Schildern"></div>
      <span class="badge">WIR FREUEN UNS AUF DICH</span>
      <div class="box"><b>Fragen?</b>Viele Antworten findet ihr auch in den FAQs – Du kannst Dich aber auch gerne direkt an uns wenden.
        <div class="row"><svg viewBox="0 0 6 6"><path d="M1 .5h1.3l.5 1.4-.8.6a3 3 0 0 0 1.5 1.5l.6-.8 1.4.5V5A.5.5 0 0 1 5 5.5 4.5 4.5 0 0 1 .5 1 .5.5 0 0 1 1 .5z" fill="#fff"/></svg>0251 555 01 234</div>
        <div class="row"><svg viewBox="0 0 6 6"><rect x=".5" y="1" width="5" height="4" fill="none" stroke="#fff" stroke-width=".6"/><path d="M.5 1l2.5 2 2.5-2" fill="none" stroke="#fff" stroke-width=".6"/></svg>personal@kistenbote.de</div>
      </div>
    </div>
  </section>
  <div class="foot"><span>© kistenbote GmbH</span><span>IMPRESSUM</span><span>DATENSCHUTZ</span></div>
</div>

<!-- FAQ page -->
<div class="page sub-page p4">
  <div class="nav"><span class="brand"><i></i>kistenbote</span><ul><li>UNTERNEHMEN</li><li>JOBS</li><li>FAQ</li></ul><span class="shop">UNSER SHOP</span></div>
  <section class="sec" style="padding-bottom:8px">
    <span class="rule"></span>
    <h2 class="h h-green">Häufige Fragen</h2>
    <p class="sub" style="font-size:4px">Bitte wähle Deinen Bereich.</p>
    <div class="cards" style="gap:14px">
      <div class="jobcard" style="width:70px"><div class="photo ph-office" style="height:44px" role="img" aria-label="Kollegen im Büro"></div><div class="lab" style="font-size:3.6px;padding:3px 0">CORPORATE</div></div>
      <div class="jobcard" style="width:70px"><div class="photo ph-warehouse" style="height:44px" role="img" aria-label="Mitarbeiter im Lager"></div><div class="lab" style="font-size:3.6px;padding:3px 0">AUSLIEFERUNG /LAGER</div></div>
    </div>
    <p style="font-size:4px;color:var(--dark);margin-top:10px">KATEGORIEN</p>
  </section>
  <div class="faq">
    <div class="row"><span>+</span>VOR DEINER BEWERBUNG</div>
    <p><b>Welche Unterlagen brauche ich für die Bewerbung?</b><br>Ein kurzer Lebenslauf reicht völlig aus. Zeugnisse kannst Du gerne mitschicken, sie sind aber kein Muss.</p>
    <p><b>Muss ich Erfahrung im Getränkehandel haben?</b><br>Nein. Wir arbeiten Dich in Ruhe ein und Du lernst alle Abläufe direkt im Team kennen.</p>
    <p><b>Brauche ich einen Führerschein?</b><br>Für die Auslieferung benötigst Du einen Führerschein der Klasse B. Im Lager ist das nicht nötig.</p>
    <p><b>Wie schnell bekomme ich eine Rückmeldung?</b><br>In der Regel melden wir uns innerhalb weniger Tage bei Dir.</p>
    <div class="row"><span>+</span>ARBEITEN BEI KISTENBOTE</div>
  </div>
  <div class="foot" style="position:absolute;bottom:0;left:0;right:0"><span>© kistenbote GmbH</span><span>IMPRESSUM</span><span>DATENSCHUTZ</span></div>
</div>

</body>
</html>
```